Fantasy Football UX Style Guide & Sample Pages (TKB - not soccer)

Happy April designers!! We are looking to establish a relationship with a killer designer who can work with us on establishing an exciting, professional UX that is delivers a great experience and leverages the powerful technologies of react.js and other 2015 advancements.

Our ideal design team can be one or more people -- but is responsive to feedback, has "no ego" in his/her designs and is willing to go the extra mile to get the job done well. We expect several iterations before any design is considered final. If this excites you - jump in!! If you think working together in an iterative fashion would frustrate you -- please stop now. We will give lots of feedback and ideas. The UX resulting is very important to us.

The site that we are building is related to TKB football. If you have no experience watching American TKB Football -- please stop reading. If you enjoy this game and would like to design UX elements that have an affinity -- please join this design contest.

As a starter project -- we are going to ask that someone review the designs that we have received for a variety of project design competitions. You will notice that they are all pretty disjointed (from our opinion) and also a little 2005 from a design perspective. The winner from this competition will assemble an accepted, killer design that will bring all of these "pages" together into a common design. We would like to see each page in the concept.

Ultimately, what this amounts to is a common style guide that delivers on the strength of the existing brand & logo (files 1 & 2) --- and hopefully -- takes it, and the pages to the next level.

Please note: While our ideal partner will give us an iteration of each page in the new design style guide -- the style guide itself is what is the most important deliverable. We won't expect every page to be perfect. We realize that will take some additional project work.

Target Market(s)

fantasy sports players

Industry/Entity Type

Work

Number of Pages Required

5+ page

Font styles to use
Serif
Sans Serif

Colors
ec1f27
ffffff
161616
959595

Requirements
Must have
• Must Have:
• - A strong sense of brand (please feel free to ask questions; logo is in file 1 & 2)
• - A strong understanding of what resonates with fantasy football players
• - A STYLE GUIDE -- I mention this above but this our primary deliverable for this project. We are looking for an awesome style guide that can be used to deliver any page / mobile app regardless of what is on it. [file attached for example of what a proper style guide looks like. We would like to see this expanded upon]
• - We are looking to see the style guide applied to a variety of page types (examples are shared in the files below -- home page, blog home page, blog item page, specific pages of importance.) This will give us a sense of how the style guide holds up and if we need some new areas addressed in it.
• - We recognize that each page doesn't have to be pixel perfect, and we are willing to take that on as additional project work if the designer would like it.
• - An design that is "easy to read" but conveys excitement
• - We deal with a lot of "sports analytics" so understanding what makes for a good chart is helpful. (if you want to use examples from d3, that is even better)
• - An understanding for how to visualize date & trends in data (see above)
• - A modern REACT.JS like look; not looking for styles from 10 years ago
Nice to have
• - Fresh new takes on the layouts included here.
• - Suggestions for how to make the logo more 2015
• - Creative, visionary ideas
• - Questions for what the screens attached are meant to portray (we'd rather you ask)
Should not have
• - A new logo or color palette. We like what we have and have an established presence here.
• - We are looking for pure, kick-ass design at this point. We don't want it coded.
• - There are many elements that we like from the concept pages below. You don't have to redesign everything. What we don't like is that the UX is not great, and there is no common styling. Also the design itself feels a little "dated" and "dark" in some areas. We are hoping for something more exciting and fresh.

```html
<!DOCTYPE html>
<html lang="en">
<head>
<meta charset="utf-8">
<title>Endzone Oracle — Fantasy Football</title>
<link href="https://fonts.googleapis.com/css2?family=Arimo:wght@400;700&display=swap" rel="stylesheet">
<style>
:root{
  --red:#ec1f27;
  --red-soft:#f05a5f;
  --pink:#f7a1a4;
  --pink-line:#f3b3b5;
  --ink:#161616;
  --bar:#3d3d3d;
  --grey:#959595;
  --table-head:#555555;
  --light:#ececec;
  --mid:#d9d9d9;
  --white:#ffffff;
  --text:#333333;
}
*{box-sizing:border-box;margin:0;padding:0}
html,body{width:735px;height:1200px;overflow:hidden;background:var(--white)}
body{font-family:"Arimo",Arial,sans-serif;color:var(--text)}
.canvas{position:relative;width:735px;height:1200px;overflow:hidden;background:var(--light)}
.abs{position:absolute}

/* top bar */
.topbar{left:0;top:0;width:735px;height:29px;background:#1b1b1b}
.brand{left:189px;top:6px;display:flex;align-items:center;gap:5px}
.brand-square{width:17px;height:17px;background:var(--red)}
.brand-name{color:var(--white);font-weight:700;font-size:9px;letter-spacing:.4px;line-height:1.1}
.brand-tag{color:var(--grey);font-weight:700;font-size:5px;letter-spacing:.3px}
.topnav{left:332px;top:10px;display:flex;gap:8px;color:var(--white);font-size:6px;white-space:nowrap}
.auth{left:489px;top:8px;display:flex}
.auth span{font-size:6px;padding:2px 5px;height:10px;line-height:6px}
.btn-login{background:var(--white);color:var(--ink)}
.btn-register{background:var(--red);color:var(--white)}

.mainnav{left:0;top:29px;width:735px;height:19px;background:var(--bar)}
.mainnav ul{position:absolute;left:189px;top:6px;display:flex;gap:10px;list-style:none;color:var(--white);font-size:6px}
.search{left:472px;top:33px;width:74px;height:11px;background:var(--white);font-size:5px;color:#aaa;padding:3px 3px}
.search svg{position:absolute;right:3px;top:2px}

/* hero */
.hero{left:0;top:48px;width:735px;height:234px;background:radial-gradient(ellipse at 45% 40%,#3e5a7a 0%,#1d2d44 45%,#0d1522 100%)}
.hero-photo{left:170px;top:48px;width:240px;height:234px;background:linear-gradient(90deg,#2a3a5c 0%,#3d4e6e 40%,#2f6b3a 65%,#c9a22a 100%);opacity:.85}
.hero-card{left:390px;top:77px;width:156px;height:176px;background:rgba(40,44,52,.92);border:1px solid #6a6e76;border-radius:2px;color:var(--white)}
.hero-thumb{left:10px;top:13px;width:34px;height:35px;background:linear-gradient(#6b4a36,#3a2418)}
.hero-name{left:50px;top:14px;font-size:10px;letter-spacing:.2px;white-space:nowrap}
.hero-role{left:50px;top:28px;font-size:5.5px}
.hero-rank{left:51px;top:38px;font-size:9px;color:var(--red)}
.hero-title{left:9px;top:55px;width:140px;font-size:5.6px;font-weight:700;line-height:1.25}
.hero-quote{left:9px;top:74px;width:140px;font-size:5.3px;line-height:1.38}
.btn-red{background:var(--red);color:var(--white);font-size:5.8px;padding:3px 5px;border-radius:1px}
.hero-more{left:9px;top:149px}
.dots{left:510px;top:271px;display:flex;gap:3px}
.dots i{width:5px;height:5px;border:1px solid var(--red);border-radius:50%}
.dots i.on{background:var(--red)}

/* rankings */
.band-mid{left:0;width:735px;background:var(--mid)}
.section-title{width:735px;left:0;text-align:center;font-size:10.5px;color:#333;font-weight:400}
.pos-item{width:64px;text-align:center}
.pos-ring{width:60px;height:60px;margin:0 auto;border-radius:50%;background:var(--white);border:3px solid #d0d0d0;display:flex;align-items:center;justify-content:center}
.pos-ring .inner{width:46px;height:46px;border:2px solid var(--red);border-radius:50%;display:flex;align-items:center;justify-content:center}
.pos-item.active .pos-ring{border-color:var(--red-soft)}
.pos-label{margin-top:4px;font-size:7px;color:#444;white-space:nowrap}
.pos-item.active .pos-label{background:var(--pink);color:var(--white);padding:1px 0}

.rank-table{left:188px;top:397px;width:358px;border-collapse:collapse;font-size:5.6px;color:#333;background:#f4f4f4;border-left:1px solid var(--pink-line);border-right:1px solid var(--pink-line)}
.rank-table th{background:var(--table-head);color:var(--white);font-weight:400;font-size:6.3px;height:25px;text-align:left;padding-left:9px;line-height:1.2}
.rank-table td{height:24px;border-bottom:1px solid #e3c7c8;padding-left:9px}
.rank-foot{left:188px;top:566px;width:358px;height:24px;background:var(--pink);font-size:5.6px;color:#5a2a2c}
.rank-foot .links{position:absolute;left:48px;top:9px;display:flex;gap:13px}
.rank-foot .show{position:absolute;right:15px;top:6px;background:var(--white);color:#333;padding:3px 4px;font-size:6px}

/* videos */
.videos-title{left:188px;top:609px;font-size:10px;color:#333;font-weight:400}
.video-main{left:189px;top:624px;width:175px;height:102px;background:linear-gradient(135deg,#3a6a3a,#2a3c7a 55%,#6a2a2a)}
.video-bar{left:189px;top:711px;width:175px;height:15px;background:rgba(20,20,20,.85)}
.video-date{left:370px;top:622px;font-size:6px;font-weight:700;color:#333}
.thumb{width:51px;height:31px}
.btn-more-videos{left:370px;top:715px;font-size:6px}

/* gallery */
.gallery-tabs{left:188px;top:766px;width:358px;height:16px;background:var(--pink);font-size:5.8px}
.gallery-tabs span{position:absolute;top:5px;color:#5a2a2c}
.gallery-tabs .active{left:0;top:0;height:16px;background:var(--red-soft);color:var(--white);padding:5px 6px}
.arrow-box{top:4px;width:8px;height:8px}
.gal-img{top:788px;width:86px;height:57px}

/* blog */
.blog-card{width:173px;height:61px;background:var(--white);border:1px solid var(--pink-line)}
.blog-card .pic{position:absolute;left:3px;top:3px;width:49px;height:54px}
.blog-card h3{position:absolute;left:56px;top:4px;font-size:5.8px;font-weight:700;color:var(--ink)}
.blog-card p{position:absolute;left:56px;top:14px;width:112px;font-size:5.3px;line-height:1.4;color:#444}
.btn-blog{left:189px;top:1030px}

/* partners */
.partners{left:0;top:1054px;width:735px;height:30px;background:var(--mid)}
.partner{top:1063px;height:12px;background:#b8b8b8;border-radius:2px}

/* footer */
.footer{left:0;top:1086px;width:735px;height:104px;background:#1a1a1a}
.footer-brand{left:198px;top:1110px;width:90px;text-align:center}
.footer-brand .sq{width:38px;height:38px;margin:0 auto 6px;border:5px solid #d8d8d8;border-radius:6px}
.footer-brand .name{font-size:8.5px;font-weight:700;letter-spacing:.6px;color:#e8e8e8}
.footer-rule{left:298px;top:1106px;width:1px;height:70px;background:#444}
.footer-h{font-size:7px;color:var(--white)}
.quick{left:309px;top:1108px;color:var(--white)}
.quick ul{margin-top:8px;padding-left:8px;font-size:5.8px;line-height:1.75}
.contact-row{font-size:5.8px;display:flex;align-items:center;gap:6px;color:var(--white)}
.email-form{left:393px;top:1157px;display:flex}
.email-form span{height:9px;font-size:4.5px;padding:2px 3px}
.email-field{width:48px;background:var(--white);color:#999}
.email-btn{background:var(--red);color:var(--white)}
.social{left:494px;top:1126px;display:flex;gap:2px}
.social i{width:10px;height:10px;border-radius:50%}
.bottom-bar{left:0;top:1190px;width:735px;height:10px;background:var(--red)}
.copyright{left:191px;top:1192px;font-size:4.2px;color:#f6c9ca}
</style>
</head>
<body>
<div class="canvas">

  <header class="abs topbar"></header>
  <div class="abs brand">
    <span class="brand-square"></span>
    <div><div class="brand-name">ENDZONE ORACLE</div><div class="brand-tag">Win. Fantasy Football</div></div>
  </div>
  <nav class="abs topnav"><span>WEEKLY RANKINGS</span><span>TKB TEAMS</span><span>PRESEASON</span></nav>
  <div class="abs auth"><span class="btn-login">Login</span><span class="btn-register">Register</span></div>

  <nav class="abs mainnav"><ul><li>HOME</li><li>ABOUT US</li><li>LATEST NEWS</li><li>VIDEOS</li><li>BLOG</li><li>CONTACT US</li></ul></nav>
  <div class="abs search">Search
    <svg width="7" height="7" viewBox="0 0 10 10"><circle cx="4" cy="4" r="3" fill="none" stroke="#ec1f27" stroke-width="1.4"/><line x1="6.3" y1="6.3" x2="9" y2="9" stroke="#ec1f27" stroke-width="1.4"/></svg>
  </div>

  <section class="abs hero"></section>
  <div class="abs hero-photo" role="img" aria-label="Two football players in uniform, one carrying the ball, against a stormy backdrop with red lightning"></div>
  <article class="abs hero-card">
    <div class="abs hero-thumb" role="img" aria-label="Player headshot"></div>
    <div class="abs hero-name">JULIEN ARDENT</div>
    <div class="abs hero-role">FORWARD PLAYER</div>
    <div class="abs hero-rank">#5 QB</div>
    <div class="abs hero-title">2015 Fantacy Football Quaterback Consensus Rankings</div>
    <p class="abs hero-quote">“Let's talk about lighting, specifically for mood,” writes Corwin on his blog. “The eye finds discomfort and intimidation in the unknown and the unknown is where the light is not. The approach to making a subject intimidating should not be a mass of lights cranked to 11, but a single focus of direction where one light dominates and the remaining support the fear. An example of this that I shot a while back is this portrait of a football player.”</p>
    <span class="abs btn-red hero-more">Read More</span>
  </article>
  <div class="abs dots"><i></i><i></i><i class="on"></i><i></i></div>

  <!-- weekly rankings -->
  <div class="abs band-mid" style="top:352px;height:245px"></div>
  <h2 class="abs section-title" style="top:300px">Weekly Rankings</h2>

  <div class="abs pos-item active" style="left:190px;top:324px">
    <div class="pos-ring"><div class="inner">
      <svg width="30" height="20" viewBox="0 0 30 20"><rect x="1" y="1" width="28" height="18" fill="none" stroke="#ec1f27" stroke-width="1.4"/><line x1="15" y1="1" x2="15" y2="19" stroke="#ec1f27" stroke-width="1.2"/><circle cx="15" cy="10" r="3" fill="#ec1f27"/><rect x="1" y="6" width="5" height="8" fill="none" stroke="#ec1f27"/><rect x="24" y="6" width="5" height="8" fill="none" stroke="#ec1f27"/></svg>
    </div></div>
    <div class="pos-label">Quater back</div>
  </div>
  <div class="abs pos-item" style="left:262px;top:324px">
    <div class="pos-ring"><div class="inner">
      <svg width="26" height="26" viewBox="0 0 26 26"><ellipse cx="13" cy="13" rx="11" ry="6.5" transform="rotate(-35 13 13)" fill="#ec1f27"/><line x1="9" y1="16" x2="17" y2="10" stroke="#fff" stroke-width="1.2"/><line x1="11" y1="11.5" x2="12.5" y2="14" stroke="#fff"/><line x1="13" y1="10.5" x2="14.5" y2="13" stroke="#fff"/><line x1="15" y1="9" x2="16.5" y2="11.5" stroke="#fff"/></svg>
    </div></div>
    <div class="pos-label">Running Back</div>
  </div>
  <div class="abs pos-item" style="left:336px;top:324px">
    <div class="pos-ring"><div class="inner">
      <svg width="26" height="26" viewBox="0 0 26 26"><path d="M3 20Q8 6 20 6" fill="none" stroke="#ec1f27" stroke-width="2.2"/><path d="M16 2L22 6L16 10Z" fill="#ec1f27"/><circle cx="5" cy="21" r="2.2" fill="#ec1f27"/></svg>
    </div></div>
    <div class="pos-label">Wide Reciever</div>
  </div>
  <div class="abs pos-item" style="left:408px;top:324px">
    <div class="pos-ring"><div class="inner">
      <svg width="26" height="26" viewBox="0 0 26 26"><path d="M13 2L22 5V12Q22 20 13 24Q4 20 4 12V5Z" fill="none" stroke="#ec1f27" stroke-width="2"/><path d="M9 13L12 16L17 9" fill="none" stroke="#ec1f27" stroke-width="2"/></svg>
    </div></div>
    <div class="pos-label">Tight End</div>
  </div>
  <div class="abs pos-item" style="left:481px;top:324px">
    <div class="pos-ring"><div class="inner">
      <svg width="26" height="26" viewBox="0 0 26 26"><path d="M5 3V12H21V3M13 12V24" fill="none" stroke="#ec1f27" stroke-width="2.2"/><circle cx="13" cy="6" r="2.5" fill="#ec1f27"/></svg>
    </div></div>
    <div class="pos-label">Kicker</div>
  </div>

  <table class="abs rank-table">
    <colgroup><col style="width:34px"><col style="width:43px"><col style="width:63px"><col style="width:53px"><col style="width:53px"><col style="width:55px"><col style="width:57px"></colgroup>
    <thead><tr><th>Rank</th><th>Position</th><th>Player Name</th><th>Team</th><th>1Day<br>Movement</th><th>2Day<br>Movement</th><th>3Day<br>Movement</th></tr></thead>
    <tbody>
      <tr><td>1</td><td>QB</td><td>Dale Brant</td><td>Harbormen</td><td>------</td><td>------</td><td>------</td></tr>
      <tr><td>2</td><td>WR</td><td>Marlon Bates</td><td>Forgers</td><td>------</td><td>------</td><td>------</td></tr>
      <tr><td>3</td><td>QB</td><td>Glen Barlow</td><td>Stallions</td><td>------</td><td>------</td><td>------</td></tr>
      <tr><td>4</td><td>WR</td><td>Vance Burke</td><td>Wardens</td><td>------</td><td>------</td><td>------</td></tr>
      <tr><td>5</td><td>WR</td><td>Sid Baxter</td><td>Millers</td><td>------</td><td>------</td><td>------</td></tr>
      <tr><td>6</td><td>WR</td><td>Quentin Boyd</td><td>Drovers</td><td>------</td><td>------</td><td>------</td></tr>
    </tbody>
  </table>
  <div class="abs rank-foot">
    <div class="links">
      <span><svg width="5" height="5" viewBox="0 0 5 5"><path d="M0 0L5 2.5L0 5Z" fill="#fff"/></svg>&nbsp; Our Other Rankings</span>
      <span>PPR Scoring</span><span>Standerd Scoring</span>
    </div>
    <span class="show">SHOW ALL DATA</span>
  </div>

  <!-- videos -->
  <h2 class="abs videos-title">latest videos</h2>
  <div class="abs video-main" role="img" aria-label="Video still of a tackle during a football game"></div>
  <svg class="abs" style="left:264px;top:665px" width="22" height="22" viewBox="0 0 22 22"><circle cx="11" cy="11" r="9.5" fill="none" stroke="#fff" stroke-width="1.5"/><path d="M9 7L15 11L9 15Z" fill="#fff"/></svg>
  <div class="abs video-bar">
    <svg class="abs" style="left:9px;top:4px" width="6" height="7" viewBox="0 0 6 7"><path d="M0 0L6 3.5L0 7Z" fill="#fff"/></svg>
    <div class="abs" style="left:25px;top:6px;width:120px;height:3px;background:#555;border-radius:2px"></div>
    <div class="abs" style="left:152px;top:4px;font-size:5px;color:#4aa8e0;font-weight:700">HD</div>
  </div>
  <div class="abs video-date">April10 2015</div>
  <div class="abs thumb" style="left:370px;top:635px;background:linear-gradient(#3a5a9a,#3a7a3a)" role="img" aria-label="Game action video thumbnail"></div>
  <div class="abs thumb" style="left:431px;top:635px;background:linear-gradient(#555,#3a7a3a)" role="img" aria-label="Player celebrating video thumbnail"></div>
  <div class="abs thumb" style="left:493px;top:635px;background:linear-gradient(#8a3a2a,#3a3a4a)" role="img" aria-label="Quarterback throwing video thumbnail"></div>
  <div class="abs thumb" style="left:370px;top:678px;background:linear-gradient(#4a5a7a,#3a6a3a)" role="img" aria-label="Team on the field video thumbnail"></div>
  <div class="abs thumb" style="left:431px;top:678px;background:linear-gradient(#6a2a2a,#2a2a2a)" role="img" aria-label="Coach at press conference video thumbnail"></div>
  <div class="abs thumb" style="left:493px;top:678px;background:linear-gradient(#2a3a2a,#2f6a2f)" role="img" aria-label="Player in green jersey video thumbnail"></div>
  <span class="abs btn-red btn-more-videos">More Videos</span>

  <!-- gallery -->
  <h2 class="abs section-title" style="top:747px">Gallery</h2>
  <div class="abs band-mid" style="top:762px;height:89px"></div>
  <div class="abs gallery-tabs">
    <span class="active">Match Highlights</span>
    <span style="left:68px">Players</span>
    <span style="left:109px">photo shoots</span>
    <svg class="abs arrow-box" style="left:335px" viewBox="0 0 8 8"><rect width="8" height="8" fill="#161616"/><path d="M5 2L3 4L5 6" fill="none" stroke="#fff"/></svg>
    <svg class="abs arrow-box" style="left:345px" viewBox="0 0 8 8"><rect width="8" height="8" fill="#ec1f27"/><path d="M3 2L5 4L3 6" fill="none" stroke="#fff"/></svg>
  </div>
  <div class="abs gal-img" style="left:188px;background:linear-gradient(#5a6a8a,#3a7a3a)" role="img" aria-label="Player celebrating on the field"></div>
  <div class="abs gal-img" style="left:278px;background:linear-gradient(#3a4a6a,#3a6a3a)" role="img" aria-label="Players lined up during a match"></div>
  <div class="abs gal-img" style="left:369px;background:linear-gradient(#2a3a2a,#2f6a2f 60%,#c9a22a)" role="img" aria-label="Player in green and yellow uniform"></div>
  <div class="abs gal-img" style="left:459px;background:linear-gradient(#8a2a2a,#3a3a4a)" role="img" aria-label="Quarterback throwing during warm-up"></div>

  <!-- blog -->
  <h2 class="abs section-title" style="top:866px">Recent Blog</h2>
  <svg class="abs" style="left:189px;top:944px" width="357" height="19" viewBox="0 0 357 19"><path d="M150 0H174L173 19H0Z" fill="#f7a1a4"/><path d="M184 0H210L357 19H184Z" fill="#f7a1a4"/></svg>
  <article class="abs blog-card" style="left:189px;top:883px">
    <div class="pic" role="img" aria-label="Player portrait" style="background:linear-gradient(#4a5a7a,#2a2a3a)"></div>
    <h3>Lorem Ipsum is simply dummy text</h3>
    <p>Lorem Ipsum is simply dummy text of the printing and typesetting industry. Lorem Ipsum has been the industry's standard dummy text ever since the 1500s, when an unknown printer..</p>
  </article>
  <article class="abs blog-card" style="left:373px;top:883px">
    <div class="pic" role="img" aria-label="Coach portrait" style="background:linear-gradient(#6a2a2a,#1a1a1a)"></div>
    <h3>Lorem Ipsum is simply dummy text</h3>
    <p>Lorem Ipsum is simply dummy text of the printing and typesetting industry. Lorem Ipsum has been the industry's standard dummy text ever since the 1500s, when an unknown printer..</p>
  </article>
  <article class="abs blog-card" style="left:189px;top:963px">
    <div class="pic" role="img" aria-label="Analyst portrait" style="background:linear-gradient(#7a7a7a,#3a3a4a)"></div>
    <h3>Lorem Ipsum is simply dummy text</h3>
    <p>Lorem Ipsum is simply dummy text of the printing and typesetting industry. Lorem Ipsum has been the industry's standard dummy text ever since the 1500s, when an unknown printer..</p>
  </article>
  <article class="abs blog-card" style="left:373px;top:963px">
    <div class="pic" role="img" aria-label="Quarterback at practice" style="background:linear-gradient(#8a2a2a,#3a3a4a)"></div>
    <h3>Lorem Ipsum is simply dummy text</h3>
    <p>Lorem Ipsum is simply dummy text of the printing and typesetting industry. Lorem Ipsum has been the industry's standard dummy text ever since the 1500s, when an unknown printer..</p>
  </article>
  <span class="abs btn-red btn-blog">Recent Blog</span>

  <!-- partners -->
  <div class="abs partners"></div>
  <div class="abs partner" style="left:197px;width:52px"></div>
  <div class="abs partner" style="left:266px;width:30px"></div>
  <div class="abs partner" style="left:321px;width:42px"></div>
  <div class="abs partner" style="left:391px;width:28px"></div>
  <div class="abs partner" style="left:445px;width:37px"></div>
  <div class="abs partner" style="left:504px;width:34px"></div>

  <!-- footer -->
  <footer class="abs footer"></footer>
  <div class="abs footer-brand"><div class="sq"></div><div class="name">ENDZONE ORACLE</div></div>
  <div class="abs footer-rule"></div>
  <div class="abs quick">
    <div class="footer-h">Quick Navigation</div>
    <ul><li>About Us</li><li>Latest News</li><li>Videos</li><li>Blog</li><li>Contact</li></ul>
  </div>
  <div class="abs footer-h" style="left:394px;top:1108px">Get in touch</div>
  <div class="abs contact-row" style="left:395px;top:1125px">
    <svg width="7" height="7" viewBox="0 0 10 10"><path d="M2 0L4 2.5L3 4Q4.5 6 6 7L7.5 6L10 8L8.5 10Q3 9 0 2Z" fill="#fff"/></svg>800-555-0199</div>
  <div class="abs contact-row" style="left:394px;top:1141px">
    <svg width="9" height="6" viewBox="0 0 9 6"><rect x=".5" y=".5" width="8" height="5" fill="none" stroke="#fff"/><path d="M.5 .5L4.5 3.5L8.5 .5" fill="none" stroke="#fff"/></svg>info@endzone-oracle.com</div>
  <div class="abs email-form"><span class="email-field">Email address</span><span class="email-btn">SIGN UP</span></div>
  <div class="abs footer-h" style="left:495px;top:1108px">Follow Us</div>
  <div class="abs social"><i style="background:#3b5a9a"></i><i style="background:#3aa7e0"></i><i style="background:#1e78b4"></i><i style="background:#e0452a"></i></div>
  <div class="abs bottom-bar"></div>
  <div class="abs copyright">Copyright © 2007-2015 Endzone-oracle. All rights reserved.</div>

</div>
</body>
</html>
```